letter drop flyer

a6 flyer for letterdropping the suburb

I have attached my last one, so something along these lines but my phone number and business card is now different.

```html
<!DOCTYPE html>
<html lang="en">
<head>
<meta charset="utf-8">
<title>Harbour Lane Realty – Letterbox Flyer</title>
<link href="https://fonts.googleapis.com/css2?family=Arimo:wght@400;700&display=swap" rel="stylesheet">
<style>
  :root {
    --page-bg: #8a8a8a;
    --paper: #ffffff;
    --brand-blue: #0a67a8;
    --brand-blue-light: #2e8fd0;
    --sketch-light: #fbf4dc;
    --sketch-warm: #e9cf86;
    --figure-tone: #e8eef4;
    --figure-dark: #b9c7d3;
    --accent-orange: #f3a11c;
    --silver-light: #fafafa;
    --silver-dark: #c9c9c9;
    --ink: #1d1d1d;
  }
  html, body {
    margin: 0;
    padding: 0;
    width: 1200px;
    height: 1000px;
    overflow: hidden;
    background: var(--page-bg);
    font-family: "Arimo", Arial, sans-serif;
  }
  .flyer {
    position: absolute;
    left: 290px;
    top: 61px;
    width: 620px;
    height: 877px;
    background: var(--paper);
    overflow: hidden;
    box-shadow: 0 6px 18px rgba(0,0,0,0.25);
  }
  .house-sketch {
    position: absolute;
    left: 0; top: 0;
    width: 430px; height: 370px;
    background: radial-gradient(ellipse at 40% 55%, var(--sketch-warm) 0%, var(--sketch-light) 70%);
  }
  .offer-band {
    position: absolute;
    left: 0; top: 370px;
    width: 620px; height: 400px;
    background: var(--brand-blue);
  }
  .offer-band svg { position: absolute; right: 0; bottom: 0; }
  .agent-panel {
    position: absolute;
    left: 430px; top: 0;
    width: 190px; height: 450px;
    background: var(--paper);
    border-bottom-left-radius: 40px;
  }
  .agent-figure {
    position: absolute;
    left: 20px; top: 40px;
    width: 150px; height: 300px;
    border-radius: 70px 70px 20px 20px;
    background: linear-gradient(180deg, var(--figure-tone) 0%, var(--figure-dark) 100%);
  }
  .agent-card {
    position: absolute;
    left: 28px; top: 22px;
    width: 270px;
    padding: 18px 0 20px;
    background: var(--paper);
    box-shadow: 0 3px 10px rgba(0,0,0,0.25);
    text-align: center;
  }
  .brand {
    display: flex;
    align-items: center;
    justify-content: center;
    gap: 8px;
    margin-bottom: 16px;
  }
  .brand-square { width: 20px; height: 20px; background: var(--brand-blue); }
  .brand-name { font-size: 21px; font-weight: 700; color: var(--brand-blue); white-space: nowrap; }
  .agent-name { font-size: 17px; font-weight: 700; color: var(--ink); margin: 0; }
  .agent-title { font-size: 17px; font-weight: 700; color: var(--brand-blue); margin: 2px 0 8px; }
  .agent-phone { font-size: 18px; font-weight: 700; color: var(--brand-blue); margin: 4px 0 0; }
  .seal {
    position: absolute;
    left: 462px; top: 330px;
    width: 140px; height: 140px;
    border-radius: 50%;
    background: radial-gradient(circle at 40% 35%, var(--silver-light) 0%, var(--silver-dark) 100%);
    box-shadow: 0 3px 8px rgba(0,0,0,0.3);
    display: flex;
    align-items: center;
    justify-content: center;
    text-align: center;
    color: var(--accent-orange);
    font-weight: 700;
    font-size: 16px;
    line-height: 1.2;
  }
  .acrostic {
    position: absolute;
    left: 26px; top: 385px;
    width: 560px;
    margin: 0; padding: 0;
    list-style: none;
    color: var(--paper);
  }
  .acrostic li {
    position: relative;
    height: 92px;
    padding-left: 66px;
  }
  .acrostic .initial {
    position: absolute;
    left: 0; top: -4px;
    font-size: 76px;
    font-weight: 700;
    line-height: 1;
  }
  .acrostic .line {
    display: block;
    font-size: 16px;
    font-weight: 700;
    line-height: 1.3;
    white-space: nowrap;
  }
  .acrostic .line:first-of-type { padding-top: 12px; }
  .footer {
    position: absolute;
    left: 0; top: 770px;
    width: 620px; height: 107px;
    display: flex;
    align-items: center;
    padding-left: 26px;
    box-sizing: border-box;
    color: var(--brand-blue);
    font-size: 14px;
    line-height: 1.35;
  }
  .footer-col { padding: 0 16px; }
  .footer-col:first-child { padding-left: 0; }
  .footer-col + .footer-col { border-left: 2px solid var(--brand-blue); }
</style>
</head>
<body>
  <main class="flyer">
    <div class="house-sketch" role="img" aria-label="Hand-drawn sketch of a two-storey weatherboard house in warm yellow tones"></div>

    <section class="offer-band">
      <svg width="260" height="400" viewBox="0 0 260 400" aria-hidden="true">
        <path d="M260 60 C 190 180, 140 300, 120 400 L 260 400 Z" fill="var(--brand-blue-light)" opacity="0.45"/>
      </svg>
    </section>

    <div class="agent-panel">
      <div class="agent-figure" role="img" aria-label="Illustrated sales agent holding a tablet"></div>
    </div>

    <div class="agent-card">
      <div class="brand">
        <span class="brand-square"></span>
        <span class="brand-name">Harbour Lane Realty</span>
      </div>
      <p class="agent-name">Clara Whitfield</p>
      <p class="agent-title">Sales Executive</p>
      <svg width="22" height="22" viewBox="0 0 24 24" aria-hidden="true">
        <path fill="var(--brand-blue)" d="M6.6 10.8a15.1 15.1 0 0 0 6.6 6.6l2.2-2.2a1 1 0 0 1 1-.25 11.4 11.4 0 0 0 3.6.57 1 1 0 0 1 1 1V20a1 1 0 0 1-1 1A17 17 0 0 1 3 4a1 1 0 0 1 1-1h3.5a1 1 0 0 1 1 1c0 1.25.2 2.46.57 3.6a1 1 0 0 1-.25 1z"/>
      </svg>
      <p class="agent-phone">0400 123 456</p>
    </div>

    <ul class="acrostic">
      <li><span class="initial">F</span><span class="line">or this week only I will be providing</span><span class="line">FREE Market Estimates in your street</span></li>
      <li><span class="initial">R</span><span class="line">ing your local area specialist CLARA WHITFIELD</span><span class="line">to arrange a convenient time</span></li>
      <li><span class="initial">E</span><span class="line">stimates are completely FREE with</span><span class="line">no obligation what so ever</span></li>
      <li><span class="initial">E</span><span class="line">very property will receive a written portfolio</span><span class="line">of their market estimate</span></li>
    </ul>

    <div class="seal">You Name it<br>I'll Sell It</div>

    <footer class="footer">
      <div class="footer-col">418 Marlow Street<br>Elmwood WA 6099</div>
      <div class="footer-col">Tel: (08) 9000 1200<br>Fax: (08) 9000 1290</div>
      <div class="footer-col">Email: cwhitfield@harbourlane.com.au<br>Web: www.harbourlane.com.au</div>
    </footer>
  </main>
</body>
</html>
```